Industrial Company needing new business cards

We are a newly branded Industrial trade company. We specialise in Electrical, Mechanical and Air-conditioning.

I would like to see designs single sided. Focusing on the color scheme white/red/black and possibly gray. Possibly make it a black card with white writting... but open to all designs.

I would like the design to be professional, sleek and to the point.

Industry/Entity Type

Business

Contact Information for Business Card

Tom Harwick
Managing Director / Electrician
tomwork@velnet.com.au
47 Garnet Road, Rutherford NSW 2320
Mobile: 0427115830
www.harwickindustrialgroup.com.au

Requirements
Must have
• Must be able to be sent in a manner that i can change the details for each employee.
• Our logo
Nice to have
• Would like it to somehow have " incorporating Talvo Group Pty Ltd" as this is the company we have taken over.
Should not have
• No yellow!!!
• must not simply place "talvo group" randomly on the business card. refer nice to have.

```html
<!DOCTYPE html>
<html lang="en">
<head>
<meta charset="utf-8">
<title>Harwick Industrial Group – Business Cards</title>
<link href="https://fonts.googleapis.com/css2?family=Lato:wght@400;700;900&family=Montserrat:wght@400;500&display=swap" rel="stylesheet">
<style>
  :root {
    --red: #d71f26;
    --red-dark: #a8151b;
    --black: #0b0b0b;
    --white: #ffffff;
    --ink: #1a1a1a;
    --grey: #555555;
    --page: #ecebe8;
  }
  * { box-sizing: border-box; margin: 0; padding: 0; }
  html, body { width: 1200px; height: 800px; overflow: hidden; }
  body {
    background: var(--page);
    font-family: "Lato", Arial, sans-serif;
    position: relative;
  }
  .card {
    position: absolute;
    width: 525px;
    height: 300px;
    top: 250px;
    box-shadow: 0 6px 18px rgba(0,0,0,0.18);
    overflow: hidden;
  }

  /* Front */
  .card-front { left: 50px; background: var(--red); }
  .front-panel {
    position: absolute;
    left: 26px; right: 26px; top: 30px; bottom: 26px;
    background: var(--white);
  }
  .front-brand {
    position: absolute;
    left: 0; right: 0; top: 48px;
    display: flex; flex-direction: column; align-items: center;
  }
  .brand-lockup { display: flex; align-items: center; gap: 10px; }
  .brand-square { width: 18px; height: 18px; background: var(--red); flex: none; }
  .brand-square-small { width: 12px; height: 12px; }
  .brand-name {
    font-weight: 900;
    color: var(--ink);
    text-transform: uppercase;
    letter-spacing: 0.5px;
    white-space: nowrap;
  }
  .front-brand .brand-name { font-size: 26px; }
  .brand-services {
    margin-top: 8px;
    font-size: 10px;
    letter-spacing: 1.6px;
    text-transform: uppercase;
    color: var(--grey);
    white-space: nowrap;
  }
  .front-rule {
    position: absolute;
    left: 0; right: 0; top: 150px;
    height: 3px;
    background: var(--red);
  }
  .front-incorporating {
    position: absolute;
    left: 22px; right: 22px; bottom: 16px;
    height: 44px;
    border: 1.5px solid var(--ink);
    display: flex; align-items: center; justify-content: center;
    font-family: "Montserrat", Arial, sans-serif;
    font-size: 21px;
    color: var(--ink);
    white-space: nowrap;
  }

  /* Back */
  .card-back { left: 625px; background: var(--black); }
  .back-header {
    position: absolute; left: 0; right: 0; top: 0;
    height: 92px;
    background: var(--white);
    display: flex; justify-content: space-between; align-items: center;
    padding: 0 18px 0 22px;
  }
  .back-header .brand-name { font-size: 16px; }
  .back-header .brand-services { font-size: 7px; letter-spacing: 1px; margin-top: 5px; }
  .person { text-align: right; }
  .person-name {
    font-weight: 900; font-size: 16px;
    text-transform: uppercase; color: var(--ink);
  }
  .person-name .surname { color: var(--red); }
  .person-role {
    font-size: 10px; letter-spacing: 0.4px;
    text-transform: uppercase; color: var(--ink);
    margin-top: 3px;
    white-space: nowrap;
  }
  .contact-list {
    position: absolute; left: 8px; top: 118px;
    list-style: none;
    display: flex; flex-direction: column; gap: 9px;
  }
  .contact-item {
    display: flex; align-items: stretch;
    width: 250px; height: 38px;
    background: var(--red);
    clip-path: polygon(0 0, 100% 0, 97% 100%, 0 100%);
  }
  .contact-icon {
    width: 36px;
    background: var(--red-dark);
    display: flex; align-items: center; justify-content: center;
  }
  .contact-icon svg { width: 17px; height: 17px; fill: var(--white); }
  .contact-text {
    padding-left: 10px;
    display: flex; flex-direction: column; justify-content: center;
    font-size: 10px; line-height: 1.3; color: var(--white);
    white-space: nowrap;
  }
</style>
</head>
<body>

  <section class="card card-front" aria-label="Business card front">
    <div class="front-panel">
      <div class="front-brand">
        <div class="brand-lockup">
          <span class="brand-square"></span>
          <span class="brand-name">Harwick Industrial Group</span>
        </div>
        <div class="brand-services">Electrical · Mechanical · Airconditioning</div>
      </div>
      <div class="front-rule"></div>
      <div class="front-incorporating">incorporating Talvo Group Pty Ltd</div>
    </div>
  </section>

  <section class="card card-back" aria-label="Business card back">
    <header class="back-header">
      <div class="back-brand">
        <div class="brand-lockup">
          <span class="brand-square brand-square-small"></span>
          <span class="brand-name">Harwick Industrial Group</span>
        </div>
        <div class="brand-services">Electrical · Mechanical · Airconditioning</div>
      </div>
      <div class="person">
        <div class="person-name">Tom <span class="surname">Harwick</span></div>
        <div class="person-role">Managing Director / Electrician</div>
      </div>
    </header>

    <ul class="contact-list">
      <li class="contact-item">
        <span class="contact-icon">
          <svg viewBox="0 0 24 24"><path d="M6.6 10.8a15.1 15.1 0 0 0 6.6 6.6l2.2-2.2c.3-.3.7-.4 1-.2 1.1.4 2.3.6 3.6.6.6 0 1 .4 1 1V20c0 .6-.4 1-1 1A17 17 0 0 1 3 4c0-.6.4-1 1-1h3.5c.6 0 1 .4 1 1 0 1.3.2 2.5.6 3.6.1.3 0 .7-.2 1z"/></svg>
        </span>
        <span class="contact-text">Mobile: 0427115830</span>
      </li>
      <li class="contact-item">
        <span class="contact-icon">
          <svg viewBox="0 0 24 24"><path d="M12 2a10 10 0 1 0 0 20 10 10 0 0 0 0-20zm6.9 6h-3a15.6 15.6 0 0 0-1.4-3.6A8 8 0 0 1 18.9 8zM12 4c.8 1.2 1.5 2.5 1.9 4h-3.8c.4-1.5 1.1-2.8 1.9-4zM4.3 14a8 8 0 0 1 0-4h3.4a16 16 0 0 0 0 4zm.8 2h3a15.6 15.6 0 0 0 1.4 3.6A8 8 0 0 1 5.1 16zm3-8h-3a8 8 0 0 1 4.4-3.6C8.9 5.5 8.4 6.7 8.1 8zM12 20c-.8-1.2-1.5-2.5-1.9-4h3.8c-.4 1.5-1.1 2.8-1.9 4zm2.3-6H9.7a14.7 14.7 0 0 1 0-4h4.6a14.7 14.7 0 0 1 0 4zm.2 5.6c.6-1.1 1.1-2.3 1.4-3.6h3a8 8 0 0 1-4.4 3.6zm1.8-5.6a16 16 0 0 0 0-4h3.4a8 8 0 0 1 0 4z"/></svg>
        </span>
        <span class="contact-text">
          <span>tomwork@velnet.com.au</span>
          <span>www.harwickindustrialgroup.com.au</span>
        </span>
      </li>
      <li class="contact-item">
        <span class="contact-icon">
          <svg viewBox="0 0 24 24"><path d="M12 2a7 7 0 0 0-7 7c0 5.2 7 13 7 13s7-7.8 7-13a7 7 0 0 0-7-7zm0 9.5a2.5 2.5 0 1 1 0-5 2.5 2.5 0 0 1 0 5z"/></svg>
        </span>
        <span class="contact-text">
          <span>47 Garnet Road,</span>
          <span>Brandale NSW 2418</span>
        </span>
      </li>
    </ul>
  </section>

</body>
</html>
```